Criação de Papelaria (6 itens) para Vértice & Aurora
" Funciona como dedetizadora como foco principal, possuindo a divisão dedetizadora ( controladora de pragas urbanas), a divisão hospitalar ( Comercio de equipamentos médico hospitalar), a divisão Higienização ( comércio de produtos de higiene e limpeza). O foco principal é a dedetizadora. "

```html
<!DOCTYPE html>
<html lang="pt-BR">
<head>
<meta charset="UTF-8">
<title>Vértice &amp; Aurora — Cartão de visita</title>
<link href="https://fonts.googleapis.com/css2?family=Exo+2:wght@400;600;800&family=Roboto+Condensed:wght@400;700&display=swap" rel="stylesheet">
<style>
  :root {
    --bg: #ecedeb;
    --green-dark: #0d261b;
    --green-mid: #1d4a35;
    --red: #d4141c;
    --silver: #d9dde0;
    --ink: #1b1b1b;
    --paper: #ffffff;
  }
  * { margin: 0; padding: 0; box-sizing: border-box; }
  html, body { width: 1200px; height: 1200px; overflow: hidden; }
  body {
    background: var(--bg);
    position: relative;
    font-family: "Roboto Condensed", Arial, sans-serif;
  }
  .card {
    position: absolute;
    width: 760px;
    height: 434px;
    border-radius: 30px;
    overflow: hidden;
    box-shadow: 0 14px 30px rgba(0,0,0,.18);
  }
  .card-front {
    left: 220px; top: 150px;
    background: radial-gradient(ellipse at 50% 40%, var(--green-mid) 0%, var(--green-dark) 75%);
    border-bottom: 8px solid var(--red);
  }
  .front-brand {
    position: absolute; inset: 0;
    display: flex; flex-direction: column; align-items: center; justify-content: center;
    gap: 14px;
  }
  .brand-name {
    font-family: "Exo 2", Arial, sans-serif;
    font-weight: 800;
    font-size: 58px;
    color: var(--silver);
    letter-spacing: 1px;
    text-transform: uppercase;
    line-height: 1;
  }
  .brand-tagline {
    font-family: "Exo 2", Arial, sans-serif;
    font-weight: 600;
    font-size: 20px;
    letter-spacing: 10px;
    color: var(--silver);
  }
  .card-back {
    left: 220px; top: 640px;
    background: var(--paper);
    display: flex;
  }
  .back-panel {
    width: 300px; height: 100%;
    background: radial-gradient(ellipse at 50% 35%, var(--green-mid) 0%, var(--green-dark) 80%);
    border-right: 8px solid var(--red);
    display: flex; align-items: flex-start; justify-content: center;
    padding: 110px 20px 0;
  }
  .back-panel .brand-name {
    font-size: 34px;
    text-align: center;
    line-height: 1.15;
  }
  .back-info {
    flex: 1;
    padding: 64px 44px 0 30px;
    text-align: right;
    color: var(--ink);
  }
  .person-name { font-size: 30px; font-weight: 400; letter-spacing: .5px; }
  .person-role { font-size: 15px; letter-spacing: 1px; margin-top: 2px; }
  .contact-list { list-style: none; margin-top: 48px; }
  .contact-list li {
    display: flex; justify-content: flex-end; align-items: center; gap: 12px;
    font-size: 18px; font-weight: 700; line-height: 34px;
  }
  .contact-list svg { width: 20px; height: 20px; flex: none; }
</style>
</head>
<body>

<section class="card card-front" aria-label="Frente do cartão">
  <div class="front-brand">
    <div class="brand-name">Vértice &amp; Aurora</div>
    <div class="brand-tagline">DEDETIZADORA</div>
  </div>
</section>

<section class="card card-back" aria-label="Verso do cartão">
  <div class="back-panel">
    <div class="brand-name">Vértice &amp;<br>Aurora</div>
  </div>
  <div class="back-info">
    <div class="person-name">NOME SOBRENOME</div>
    <div class="person-role">CARGO/FUNÇÃO</div>
    <ul class="contact-list">
      <li>nome@empresa.com.br
        <svg viewBox="0 0 20 20"><rect x="2" y="5" width="16" height="11" rx="1.5" fill="var(--red)"/><path d="M2.5 6 L10 11.5 L17.5 6" stroke="#fff" stroke-width="1.5" fill="none"/></svg>
      </li>
      <li>99 9999-9999
        <svg viewBox="0 0 20 20"><rect x="5" y="2" width="10" height="16" rx="2" fill="none" stroke="var(--red)" stroke-width="2"/><circle cx="10" cy="15" r="1.2" fill="var(--red)"/></svg>
      </li>
      <li>99 99999-9999
        <svg viewBox="0 0 20 20"><rect x="5" y="2" width="10" height="16" rx="2" fill="none" stroke="var(--red)" stroke-width="2"/><circle cx="10" cy="15" r="1.2" fill="var(--red)"/></svg>
      </li>
      <li>Rua do Projeto, 999
        <svg viewBox="0 0 20 20"><path d="M10 2 C6 2 4 5 4 8 C4 12 10 18 10 18 C10 18 16 12 16 8 C16 5 14 2 10 2 Z" fill="var(--red)"/><circle cx="10" cy="8" r="2.3" fill="#fff"/></svg>
      </li>
      <li>www.verticeaurora.com.br
        <svg viewBox="0 0 20 20"><circle cx="10" cy="10" r="7.5" fill="none" stroke="var(--red)" stroke-width="1.8"/><ellipse cx="10" cy="10" rx="3.2" ry="7.5" fill="none" stroke="var(--red)" stroke-width="1.5"/><line x1="2.5" y1="10" x2="17.5" y2="10" stroke="var(--red)" stroke-width="1.5"/></svg>
      </li>
    </ul>
  </div>
</section>

</body>
</html>
```